依頼詳細
川辺ふれあい会の第7号の会報の原稿を依頼する。この活動を行うボランティア募集案内で①福祉車両、買い物、病院送迎ボランティア募集 ②子ども食堂開催の際のボランティア募集 ③夏季の子ども学習指導、ゲームや遊びボランティア募集 ④高齢者居場所づくりのサロンの話し相手のボランティア募集 ⑤生活支援の一般ボランティア募集(くさとり、清掃、片付けなど)のボランテイア募集の会報の編集依頼

記載項目
デザインを見てから、説明文は後日指示します。
サイズ
A4
ページ数
片面
希望イメージ
シンプル 複雑
単色 カラフル
暗い 明るい
日常 高級
遊び心 厳粛
未来的 伝統的
女性的 男性的
希望する色
青系
納品ファイル
• 高解像度JPG (.jpg)
補足説明
データをいただき、説明文の追加等を加筆し原稿をPDFにして印刷業者へ依頼する。

```html
<!DOCTYPE html>
<html lang="ja">
<head>
<meta charset="utf-8">
<title>川辺ふれあい会 会報第7号 ボランティア募集</title>
<link rel="stylesheet" href="https://fonts.googleapis.com/css2?family=M+PLUS+Rounded+1c:wght@500;700;800;900&display=swap">
<style>
  :root{
    --blue:#1a7fd0;
    --blue-dark:#1466b0;
    --sky:#dcefff;
    --sky-mid:#b9defa;
    --orange:#f08a1c;
    --white:#ffffff;
    --ink:#27445e;
  }
  *{box-sizing:border-box;margin:0;padding:0}
  html,body{width:851px;height:1200px;overflow:hidden;background:var(--white)}
  body{font-family:"M PLUS Rounded 1c",sans-serif;color:var(--ink)}
  .sheet{position:relative;width:851px;height:1200px;background:var(--sky);overflow:hidden}

  .hero-art{position:absolute;left:270px;top:0;width:581px;height:240px;
    background:linear-gradient(180deg,#cfe9ff 0%,#e8f6e2 70%,#bfe3a8 100%)}
  .issue-box{position:absolute;left:23px;top:23px;width:247px;height:150px;background:var(--blue);
    border-radius:14px;color:var(--white);text-align:center;padding-top:14px}
  .issue-box .org{font-size:26px;font-weight:800;line-height:1.25;white-space:nowrap}
  .issue-box .no{font-size:30px;font-weight:900;margin-top:4px;line-height:1.2}
  .issue-box .no b{font-size:44px;color:#fff36b}
  .issue-meta{position:absolute;left:60px;top:184px;font-size:14px;font-weight:700;line-height:1.55;color:var(--ink)}
  .issue-meta .name{font-size:16px}
  .welcome{position:absolute;left:668px;top:82px;width:150px;height:150px;border-radius:50%;
    background:var(--orange);color:var(--white);display:flex;align-items:center;justify-content:center;
    text-align:center;font-size:16px;font-weight:800;line-height:1.35;border:4px solid var(--white)}

  .headline{position:absolute;left:255px;top:230px;width:596px;height:105px;background:var(--white);
    border-radius:18px 0 0 0;text-align:center}
  .headline .lead{font-size:19px;font-weight:800;color:var(--orange);margin-top:6px;white-space:nowrap}
  .headline h1{font-size:58px;font-weight:900;color:var(--orange);line-height:1.15;letter-spacing:1px;white-space:nowrap}
  .intro{position:absolute;left:0;top:335px;width:851px;height:62px;background:var(--blue);
    color:var(--white);font-size:15px;font-weight:700;line-height:1.6;padding:6px 28px}

  .card{position:absolute;background:var(--white);border-radius:14px;border:3px solid var(--sky-mid);padding:10px 14px}
  .card .title{display:flex;align-items:flex-start}
  .card .num{flex:none;background:var(--blue);color:var(--white);font-weight:900;font-size:18px;line-height:1.4;
    border-radius:8px;padding:0 8px;margin-right:8px;margin-top:1px}
  .card h2{font-size:20px;font-weight:800;color:var(--blue-dark);line-height:1.3;white-space:nowrap}
  .card .art{position:absolute;left:14px;right:14px;bottom:10px;height:46px;border-radius:10px;
    background:linear-gradient(90deg,#fde9cf,#d7ecfb)}
  .c1{left:23px;top:411px;width:388px;height:137px}
  .c2{left:431px;top:411px;width:397px;height:137px}
  .c3{left:23px;top:562px;width:388px;height:137px}
  .c4{left:431px;top:562px;width:397px;height:137px}
  .c5{left:23px;top:715px;width:388px;height:137px}

  .notes{position:absolute;left:434px;top:718px;width:210px;font-size:14px;font-weight:700;line-height:1.7}
  .notes p+p{margin-top:10px}
  .notes .call{color:var(--orange)}
  .helper-art{position:absolute;left:652px;top:735px;width:185px;height:255px;border-radius:90px 90px 10px 10px;
    background:linear-gradient(180deg,#f8d9b8,#9cc8ef)}

  .footer{position:absolute;left:0;top:999px;width:851px;height:201px;background:var(--blue);color:var(--white)}
  .footer .tag{position:absolute;left:28px;top:20px;background:var(--white);color:var(--blue);font-weight:800;font-size:16px;
    border-radius:6px;padding:2px 12px}
  .footer .office{position:absolute;left:175px;top:14px;font-size:30px;font-weight:900;white-space:nowrap}
  .footer .about{position:absolute;left:28px;top:68px;font-size:14px;font-weight:700;line-height:1.7;width:430px}
  .footer .hours{position:absolute;left:520px;top:78px;font-size:14px;font-weight:700;white-space:nowrap}
  .footer .tel{position:absolute;left:478px;top:110px;display:flex;align-items:center;gap:8px;
    font-size:44px;font-weight:900;white-space:nowrap;line-height:1.2}
</style>
</head>
<body>
<main class="sheet">
  <div class="hero-art" role="img" aria-label="町並みの前に並ぶ地域の人々のイラスト"></div>

  <div class="issue-box">
    <div class="org">NPO法人<br>川辺ふれあい会</div>
    <div class="no">会報第<b>7</b>号</div>
  </div>
  <div class="issue-meta">
    2022.00.00発行<br>【発行責任者】<br>理事長 <span class="name">佐野和彦</span>
  </div>
  <div class="welcome">初心者<br>興味のある方<br>大歓迎です!!</div>

  <section class="headline">
    <p class="lead">ふれあいボランティア活動しませんか</p>
    <h1>ボランティア募集!</h1>
  </section>
  <p class="intro">高齢化社会になり体力のおとろえなどで日常生活に支障をきたして困っている人たちが増えています。ぜひ仲間に入り、手助けしてください。お待ちしています。</p>

  <article class="card c1">
    <div class="title"><span class="num">01</span><h2>福祉車両、買い物、<br>病院送迎ボランティア</h2></div>
    <div class="art" role="img" aria-label="福祉車両で送迎する様子のイラスト"></div>
  </article>
  <article class="card c2">
    <div class="title"><span class="num">02</span><h2>子ども食堂開催の際の<br>ボランティア</h2></div>
    <div class="art" role="img" aria-label="子ども食堂で食事をする子どもたちのイラスト"></div>
  </article>
  <article class="card c3">
    <div class="title"><span class="num">03</span><h2>夏季の子ども学習指導、<br>ゲームや遊びボランティア</h2></div>
    <div class="art" role="img" aria-label="子どもに勉強を教える様子のイラスト"></div>
  </article>
  <article class="card c4">
    <div class="title"><span class="num">04</span><h2>高齢者居場所づくりのサロンの<br>話し相手のボランティア</h2></div>
    <div class="art" role="img" aria-label="高齢者と話す様子のイラスト"></div>
  </article>
  <article class="card c5">
    <div class="title"><span class="num">05</span><h2>生活支援の一般ボランティア<br>（くさとり、清掃、片付け等）</h2></div>
    <div class="art" role="img" aria-label="掃除道具とゴミ袋のイラスト" style="left:220px"></div>
  </article>

  <div class="notes">
    <p>どなたでもできる簡単な作業です。作業内容と曜日・時間帯等を自由に選んで活動できます。</p>
    <p>利用者さまからいただいた利用料は、ボランティアさんにすべて支払われます。<br><span class="call">お気軽にお問い合わせください!</span></p>
  </div>
  <div class="helper-art" role="img" aria-label="案内するスタッフの女性のイラスト"></div>

  <footer class="footer">
    <span class="tag">お問い合わせ</span>
    <div class="office">NPO法人 川辺ふれあい会事務局</div>
    <p class="about">明るく住みよい地域社会を作り地域に根ざした福祉の増進を図ることを目的として活動しています。</p>
    <div class="hours">月〜金（土日祝休）10:00〜15:00</div>
    <div class="tel">
      <svg width="40" height="40" viewBox="0 0 24 24" aria-hidden="true"><path fill="#fff" d="M6.6 10.8a15.1 15.1 0 0 0 6.6 6.6l2.2-2.2a1 1 0 0 1 1-.25 11.4 11.4 0 0 0 3.6.57 1 1 0 0 1 1 1V20a1 1 0 0 1-1 1A17 17 0 0 1 3 4a1 1 0 0 1 1-1h3.5a1 1 0 0 1 1 1c0 1.25.2 2.45.57 3.57a1 1 0 0 1-.25 1z"/></svg>
      0283-41-7730
    </div>
  </footer>
</main>
</body>
</html>
```